Need Letterhead Design & Matching Business Card

I have a logo that I love already. But the letterhead is less than appealing and boring. I'd like a design for my letterhead which I will match with business cards. Also, I'd like to have used fonts that are generally available, as my current letterhead uses a font named "SPACE" which nobody has unless they download it...so when a Word version is forwarded, it looks awful on the receiver's screed due to not having the font. That being said, modern is the look we like and are going for.

My business is "Halloran Brightmoor PC" - a law firm specializing in representing people who have suffered catastrophic injuries or death (plane, auto, train crashes etc.).

See attached letterhead, which has all of the pertinent information. My logo is also attached in various formats.

```html
<!DOCTYPE html>
<html lang="en">
<head>
<meta charset="utf-8">
<title>Halloran Brightmoor PC — Stationery</title>
<link href="https://fonts.googleapis.com/css2?family=Work+Sans:wght@500&family=Arimo:wght@400;700&display=swap" rel="stylesheet">
<style>
  :root {
    --ink: #000000;
    --paper: #ffffff;
    --canvas: #ffffff;
    --shadow: rgba(0,0,0,0.35);
    --dash: #777777;
  }
  * { margin: 0; padding: 0; box-sizing: border-box; }
  html, body { width: 1200px; height: 1200px; overflow: hidden; background: var(--canvas); }
  .sheet { position: relative; width: 1200px; height: 1200px; }
  .piece { position: absolute; background: var(--paper); box-shadow: 3px 4px 7px var(--shadow); overflow: hidden; }
  .mark-square { position: absolute; background: var(--ink); }
  .firm-name {
    position: absolute; font-family: "Work Sans", Arial, sans-serif; font-weight: 500;
    color: var(--ink); text-transform: uppercase; letter-spacing: 0.05em; line-height: 1.05; white-space: nowrap;
  }
  .contact-list { position: absolute; list-style: none; font-family: Arimo, Arial, sans-serif; color: var(--paper); }
  .contact-list li { display: flex; align-items: center; white-space: nowrap; }
  .contact-list svg { flex: none; }
  .address-line {
    position: absolute; left: 0; right: 0; text-align: center; font-family: Arimo, Arial, sans-serif;
    font-weight: 700; text-transform: uppercase; white-space: nowrap;
  }

  /* Letterhead */
  .letterhead { left: 50px; top: 74px; width: 527px; height: 680px; }
  .letterhead .mark-square { left: 22px; top: 18px; width: 59px; height: 59px; }
  .letterhead .firm-name { left: 89px; top: 26px; font-size: 17px; }
  .letterhead .header-band { position: absolute; left: 0; top: 0; }
  .letterhead .contact-list { left: 332px; top: 20px; font-size: 12px; }
  .letterhead .contact-list li { height: 22.5px; gap: 8px; }
  .letterhead .footer-band { position: absolute; left: 0; bottom: 0; width: 100%; height: 35px; background: var(--ink); }
  .letterhead .address-line { top: 11px; font-size: 9.6px; color: var(--paper); }

  /* Primary logo lockup */
  .lockup-square { left: 700px; top: 74px; width: 120px; height: 121px; }
  .lockup-name { left: 838px; top: 92px; font-size: 30px; }

  /* Business card front */
  .card-contact { left: 718px; top: 284px; width: 372px; height: 212px; }
  .card-contact .mark-square { left: 37px; top: 62px; width: 89px; height: 89px; }
  .card-contact .contact-band { position: absolute; left: 161px; top: 62px; right: 0; height: 89px; background: var(--ink); }
  .card-contact .contact-list { left: 28px; top: 16px; font-size: 11px; }
  .card-contact .contact-list li { height: 21px; gap: 9px; font-weight: 700; }

  /* Business card back */
  .card-brand { left: 718px; top: 542px; width: 372px; height: 212px; }
  .card-brand .mark-square { left: 69px; top: 70px; width: 73px; height: 73px; }
  .card-brand .firm-name { left: 152px; top: 82px; font-size: 19px; }
  .card-brand .address-line { top: 193px; font-size: 6.6px; color: var(--ink); }

  /* Envelope front */
  .envelope { left: 45px; top: 880px; width: 538px; height: 240px; }
  .envelope .mark-square { left: 18px; top: 20px; width: 51px; height: 51px; }
  .envelope .firm-name { left: 75px; top: 26px; font-size: 15px; }
  .envelope .address-window {
    position: absolute; left: 19px; top: 90px; width: 249px; height: 105px;
    border: 1px dashed var(--dash); border-radius: 6px;
  }

  /* Envelope back */
  .envelope-back { left: 614px; top: 880px; width: 541px; height: 240px; background: var(--ink); }
  .envelope-back .seal-square { position: absolute; left: 232px; top: 82px; width: 77px; height: 77px; background: var(--paper); }
  .envelope-back .address-line { top: 216px; font-size: 9.6px; color: var(--paper); }
</style>
</head>
<body>
<main class="sheet">

  <section class="piece letterhead" aria-label="Letterhead">
    <svg class="header-band" width="527" height="100" viewBox="0 0 527 100" aria-hidden="true">
      <polygon points="320,0 527,0 527,97 265,97" fill="var(--ink)"/>
      <rect x="0" y="94" width="270" height="3" fill="var(--ink)"/>
    </svg>
    <div class="mark-square"></div>
    <div class="firm-name">Halloran<br>Brightmoor PC</div>
    <ul class="contact-list">
      <li><svg width="14" height="14" viewBox="0 0 14 14"><circle cx="7" cy="7" r="7" fill="#fff"/><rect x="4.6" y="3" width="4.8" height="8" rx="1" fill="none" stroke="#000" stroke-width="1"/></svg>(855) 555-0142</li>
      <li><svg width="14" height="14" viewBox="0 0 14 14"><circle cx="7" cy="7" r="7" fill="#fff"/><rect x="3.5" y="4.5" width="7" height="5" fill="#000"/><path d="M3.5 4.5 L7 7.3 L10.5 4.5" fill="none" stroke="#fff" stroke-width="0.8"/></svg>md@halloranbrightmoor.com</li>
      <li><svg width="14" height="14" viewBox="0 0 14 14"><circle cx="7" cy="7" r="7" fill="#fff"/><g fill="none" stroke="#000" stroke-width="0.8"><circle cx="7" cy="7" r="4"/><ellipse cx="7" cy="7" rx="1.8" ry="4"/><path d="M3 7h8"/></g></svg>www.halloranbrightmoor.com</li>
    </ul>
    <div class="footer-band">
      <p class="address-line">Marcus Delaney, Esq. &nbsp;|&nbsp; President 4820 Larchmont Ave. &nbsp;|&nbsp; Suite 1000 Fairhaven, CA 90455</p>
    </div>
  </section>

  <div class="mark-square lockup-square"></div>
  <div class="firm-name lockup-name">Halloran<br>Brightmoor PC</div>

  <section class="piece card-contact" aria-label="Business card, contact side">
    <div class="mark-square"></div>
    <div class="contact-band">
      <ul class="contact-list">
        <li><svg width="13" height="13" viewBox="0 0 14 14"><circle cx="7" cy="7" r="7" fill="#fff"/><rect x="4.6" y="3" width="4.8" height="8" rx="1" fill="none" stroke="#000" stroke-width="1"/></svg>(855) 555-0142</li>
        <li><svg width="13" height="13" viewBox="0 0 14 14"><circle cx="7" cy="7" r="7" fill="#fff"/><rect x="3.5" y="4.5" width="7" height="5" fill="#000"/><path d="M3.5 4.5 L7 7.3 L10.5 4.5" fill="none" stroke="#fff" stroke-width="0.8"/></svg>md@halloranbrightmoor.com</li>
        <li><svg width="13" height="13" viewBox="0 0 14 14"><circle cx="7" cy="7" r="7" fill="#fff"/><g fill="none" stroke="#000" stroke-width="0.8"><circle cx="7" cy="7" r="4"/><ellipse cx="7" cy="7" rx="1.8" ry="4"/><path d="M3 7h8"/></g></svg>www.halloranbrightmoor.com</li>
      </ul>
    </div>
  </section>

  <section class="piece card-brand" aria-label="Business card, brand side">
    <div class="mark-square"></div>
    <div class="firm-name">Halloran<br>Brightmoor PC</div>
    <p class="address-line">Marcus Delaney, Esq. &nbsp;|&nbsp; President 4820 Larchmont Ave. &nbsp;|&nbsp; Suite 1000 Fairhaven, CA 90455</p>
  </section>

  <section class="piece envelope" aria-label="Envelope front">
    <div class="mark-square"></div>
    <div class="firm-name">Halloran<br>Brightmoor PC</div>
    <div class="address-window"></div>
  </section>

  <section class="piece envelope-back" aria-label="Envelope back">
    <div class="seal-square"></div>
    <p class="address-line">Marcus Delaney, Esq. &nbsp;|&nbsp; President 4820 Larchmont Ave. &nbsp;|&nbsp; Suite 1000 Fairhaven, CA 90455</p>
  </section>

</main>
</body>
</html>
```